Visitenkarten- und Briefpapier Design - Logo vorhanden!
Zielgruppe
Wir sind eine Projektentwicklungs GmbH die Grundstücke kauft, projektiert und wieder verkauft. Eine zukünftige GmbH ist für den Innenausbau von neuen Häusern (EFH,DHH,MFH) gedacht. Wir sind ebenfalls für den Vertrieb von Häusern tätig.
Unsere Zielgruppe sind Endkunden im Immobilienbereich die Grundstücke und/oder Häuser bis Schlüsselfertig kaufen möchten, sowie Grundstückseigentümer die verkaufen wollen.
Wir benötigen Visitenkarten UND Briefpapier.
Aufgabenstellung
Bitte vorhandenes Logo verwenden.
Briefpapier:
Es soll ein ansprechendes modernes Design sein. Wir lassen uns gerne überraschen und versuchen schnellstmöglich Feedback zu geben.
Visitenkarte:
Es soll ein ansprechendes modernes Design sein. Die Visitenkarte bitte mit 2 Seiten, auf der Rückseite könnten wir uns das Dunkle ZERANT Logo sehr gut vorstellen (nur Logo).

```html
<!DOCTYPE html>
<html lang="de">
<head>
<meta charset="utf-8">
<title>Zerant Briefpapier</title>
<link rel="stylesheet" href="https://fonts.googleapis.com/css2?family=Open+Sans:wght@400;600;700&display=swap">
<style>
  :root {
    --navy: #163a56;
    --green: #6fa12e;
    --ink: #4a4a4a;
    --muted: #8a8a8a;
    --rule: #cfcfcf;
    --stage: #d9d9d9;
    --paper: #ffffff;
  }
  * { box-sizing: border-box; margin: 0; padding: 0; }
  html, body { width: 1200px; height: 968px; overflow: hidden; }
  body { background: var(--stage); font-family: "Open Sans", Arial, sans-serif; color: var(--ink); }

  .letterhead {
    position: absolute; left: 275px; top: 24px;
    width: 650px; height: 920px;
    background: var(--paper);
    border-top: 4px solid var(--navy);
    box-shadow: 0 6px 24px rgba(0,0,0,.18);
    overflow: hidden;
  }

  .fold-mark { position: absolute; left: 0; width: 16px; height: 1px; background: var(--rule); }
  .fold-mark.upper { top: 300px; }
  .fold-mark.lower { top: 612px; }

  .sender-line {
    position: absolute; left: 70px; top: 190px;
    font-size: 6.5px; color: var(--ink);
    border-bottom: 1px solid var(--ink); padding-bottom: 1px;
  }

  .brand {
    position: absolute; right: 44px; top: 170px;
    display: flex; align-items: center; gap: 8px;
    font-size: 34px; font-weight: 600; letter-spacing: 4px; color: var(--navy);
  }
  .brand-dot { width: 10px; height: 10px; background: var(--green); }

  .contact {
    position: absolute; left: 482px; top: 236px;
    border-left: 1px solid var(--navy); padding-left: 14px;
    font-size: 9.5px; line-height: 1.45; color: var(--navy); font-style: normal;
  }
  .contact strong { font-weight: 700; }
  .contact .row { display: flex; align-items: center; gap: 5px; }
  .contact svg { width: 8px; height: 8px; flex: none; }

  .letter-body { position: absolute; left: 70px; top: 268px; width: 380px; font-size: 8.4px; line-height: 1.35; color: var(--ink); }
  .salutation { color: var(--muted); margin-bottom: 6px; }
  .letter-body p { margin-bottom: 8px; }

  .signature {
    width: 120px; height: 34px; margin-top: 10px;
    background: linear-gradient(90deg, #e9e9e9, #f4f4f4);
    border-radius: 4px;
  }

  .footer-rule { position: absolute; left: 70px; right: 40px; top: 700px; height: 1px; background: var(--rule); }
  .footer-info {
    position: absolute; left: 70px; right: 40px; top: 716px;
    display: flex; font-size: 8.5px; line-height: 1.4; color: var(--ink);
  }
  .footer-col { padding: 0 18px; border-left: 1px solid var(--muted); }
  .footer-col:first-child { padding-left: 0; border-left: none; }

  .footer-band {
    position: absolute; left: 0; right: 0; bottom: 0; height: 44px;
    background: var(--navy);
    border-top: 4px solid var(--green);
    display: flex; align-items: center; justify-content: flex-end;
    padding-right: 30px;
  }
  .website { font-size: 12px; letter-spacing: 1px; color: #ffffff; }
</style>
</head>
<body>
  <main class="letterhead">
    <span class="fold-mark upper"></span>
    <span class="fold-mark lower"></span>

    <div class="sender-line">Zerant GmbH | Lindenhofweg 12 | 10115 Berlin</div>

    <div class="brand"><span class="brand-dot"></span>ZERANT</div>

    <address class="contact">
      <strong>Zerant GmbH</strong><br>
      Lindenhofweg 12<br>
      10115 Berlin
      <div class="row"><svg viewBox="0 0 10 10"><path d="M2 1l2 2-1 1.5a6 6 0 0 0 2.5 2.5L7 6l2 2-1.5 1.5C4 9 1 6 .5 2.5z" fill="currentColor"/></svg>030-555 18 240</div>
      <div class="row"><svg viewBox="0 0 10 10"><rect x="2.5" y=".5" width="5" height="9" rx="1" fill="none" stroke="currentColor"/></svg>030-555 18 241</div>
      <div class="row"><svg viewBox="0 0 10 10"><rect x=".5" y="2" width="9" height="6" fill="currentColor"/><path d="M.5 2l4.5 3.5L9.5 2" fill="none" stroke="#fff" stroke-width=".8"/></svg>info@zerant.de</div>
    </address>

    <section class="letter-body">
      <div class="salutation">Herr Lindner</div>
      <p>Lorem ipsum dolor sit amet, consectetur adipiscing elit. Proin tincidunt, lectus id malesuada cursus, lorem augue egestas magna, ut mattis orci ante ut arcu. Sed mauris tellus, fermentum quis ligula nec, posuere pulvinar eros. Nam at mi quis velit pellentesque finibus. Donec lacus velit, faucibus mollis dolor nec, finibus pellentesque orci. Duis sed dictum elit, ut posuere arcu. Phasellus ac dolor et ante consequat rutrum nec nec tortor. Donec consequat, nibh sit amet pulvinar faucibus, turpis magna venenatis diam, vel pretium eros erat vestibulum nulla.</p>
      <p>Sed pretium ac enim eu viverra. Aliquam ac est eget magna convallis convallis. Aenean augue purus, finibus eget turpis quis, finibus dignissim nibh. Phasellus viverra lobortis dignissim. Duis varius turpis in sapien accumsan facilisis. Sed vehicula gravida diam a interdum. Nullam convallis ligula id erat egestas consequat. Integer consectetur ex vel aliquet iaculis. Vestibulum molestie sodales mauris, at tincidunt risus pellentesqu.</p>
      <p>Mauris facilisis, lectus at accumsan tincidunt, dui magna imperdiet sem, quis tempor est lectus eu ipsum. Praesent in fermentum nisl. Maecenas at lorem at odio interdum iaculis. Pellentesque cursus nulla nunc, ut suscipit nulla maximus et. Donec maximus rhoncus metus, vel laoreet nisi pretium sit amet. Donec posuere enim lectus, vitae aliquam augue tincidunt dignissim. Morbi vitae congue velit, quis elementum.</p>
      <div class="signature" role="img" aria-label="Handschriftliche Unterschrift"></div>
    </section>

    <div class="footer-rule"></div>
    <div class="footer-info">
      <div class="footer-col">Steuerliche ID: De184420917<br>Umsatzsteuer ID: 27 340 116 000</div>
      <div class="footer-col">Bankverbindung:<br>Nordhafen Bank Berlin</div>
      <div class="footer-col">BIC: NHBKDEBBXXX<br>IBAN: DE12 5003 0020 4410 7788 21</div>
    </div>

    <footer class="footer-band">
      <span class="website">www.zerant.de</span>
    </footer>
  </main>
</body>
</html>
```